New Television Homescreen Template

We need a new default homescreen design for our televisions. This should reflect our company branding. My company is called Wardline Systems, WLS for short. Our website is www.wlsx.example. We develop televisions and infotainment solutions for the healthcare industry. I am somewhat open to different color palettes but our company colors are blue, black, and white. Our design is constrained by the 9 buttons, however the design of the buttons can be changed. Also, there is a video box on the right side of the screen as shown, this design can also be changed.

Target Market(s)

Hospital Patients

Requirements
Must have
• PSD template.

```html
<!DOCTYPE html>
<html lang="en">
<head>
<meta charset="utf-8">
<title>Wardline Systems – Television Homescreen</title>
<link rel="stylesheet" href="https://fonts.googleapis.com/css2?family=Questrial&family=Archivo+Narrow:wght@700&family=Open+Sans:wght@400&display=swap">
<style>
  :root {
    --page: #efeeec;
    --night: #06080f;
    --white: #ffffff;
    --lime: #5fe02a;
    --cyan: #1fd6f0;
    --crimson: #c8143c;
    --yellow: #f5e60a;
    --gold: #9a7a3a;
    --teal: #1a9ea2;
    --maroon: #8a1432;
    --moss: #43603a;
    --royal: #1f5fa8;
    --navy: #123e86;
    --brand-blue: #2ea3dc;
    --ink: #2a2a2a;
  }
  * { box-sizing: border-box; margin: 0; padding: 0; }
  html, body { width: 1200px; height: 1000px; overflow: hidden; }
  body { background: var(--page); position: relative; font-family: "Questrial", sans-serif; }

  .homescreen {
    position: absolute; left: 0; top: 160px; width: 1200px; height: 678px;
    overflow: hidden; background: var(--night);
  }
  .backdrop {
    position: absolute; inset: 0;
    background:
      radial-gradient(ellipse 260px 60px at 420px 90px, rgba(31,214,240,.55), transparent 70%),
      radial-gradient(ellipse 200px 40px at 60px 160px, rgba(230,60,120,.45), transparent 70%),
      radial-gradient(ellipse 500px 90px at 900px 560px, rgba(230,40,70,.55), transparent 70%),
      radial-gradient(ellipse 360px 60px at 1000px 470px, rgba(240,190,60,.35), transparent 70%),
      radial-gradient(ellipse 300px 160px at 120px 420px, rgba(40,90,200,.45), transparent 70%),
      linear-gradient(160deg, #0b1022 0%, #05070d 45%, #140a1a 100%);
  }

  .tagline {
    position: absolute; left: 110px; top: 92px; width: 400px;
    text-align: center; color: var(--white); line-height: .88; letter-spacing: -.5px;
  }
  .tagline .line { display: block; white-space: nowrap; }
  .t-sm { font-size: 22px; }
  .t-xs { font-size: 19px; }
  .t-md { font-size: 34px; }
  .t-lg { font-size: 42px; }
  .green { color: var(--lime); }
  .cyan { color: var(--cyan); }
  .crimson { color: var(--crimson); }
  .yellow { color: var(--yellow); }

  .video-box {
    position: absolute; left: 90px; top: 279px; width: 424px; height: 239px;
    background: radial-gradient(circle at 50% 45%, #4b505a 0%, #2a2f38 35%, #1d222b 70%);
  }
  .play-button {
    position: absolute; left: 174px; top: 111px; width: 60px; height: 42px;
    border-radius: 5px; background: #e8e8e8;
  }
  .play-button svg { position: absolute; left: 21px; top: 12px; }

  .brand-band {
    position: absolute; left: 0; top: 518px; width: 640px; height: 160px;
    background: linear-gradient(90deg, #fff 0%, #fff 70%, rgba(255,255,255,0) 100%);
  }
  .brand {
    position: absolute; left: 160px; top: 538px; display: flex; align-items: center; gap: 10px;
    font-family: "Open Sans", sans-serif; color: var(--ink);
  }
  .brand-mark { width: 14px; height: 14px; background: var(--brand-blue); }
  .brand-name { font-size: 29px; letter-spacing: -.5px; }
  .brand-tagline {
    position: absolute; left: 334px; top: 581px;
    font-family: "Open Sans", sans-serif; font-size: 11px; color: var(--ink);
  }

  .menu { position: absolute; inset: 0; }
  .tile {
    position: absolute; width: 100px; height: 115px;
    clip-path: polygon(50% 0, 100% 25%, 100% 75%, 50% 100%, 0 75%, 0 25%);
    display: flex; align-items: center; justify-content: center; text-align: center;
    font-family: "Archivo Narrow", sans-serif; font-weight: 700;
    font-size: 19px; line-height: .95; color: var(--white);
  }
  .tile.small { font-size: 16px; }
  .tile.light { background: rgba(255,255,255,.86); }
  .tile.welcome { width: 128px; height: 146px; font-size: 27px; background: var(--maroon); }

  .cable { left: 739px; top: 235px; background: var(--gold); }
  .movies { left: 902px; top: 235px; background: var(--teal); }
  .welcome { left: 805px; top: 310px; }
  .campus { left: 700px; top: 337px; background: var(--moss); }
  .chart { left: 939px; top: 337px; background: var(--royal); }
  .phones { left: 641px; top: 424px; color: var(--maroon); }
  .dining { left: 761px; top: 424px; color: var(--navy); }
  .education { left: 880px; top: 424px; color: var(--maroon); }
  .services { left: 1000px; top: 424px; color: var(--royal); }
</style>
</head>
<body>
  <main class="homescreen">
    <div class="backdrop" role="img" aria-label="Blurred night-time light trails in blue, cyan, red and gold"></div>

    <h1 class="tagline">
      <span class="line"><span class="t-sm">Improving </span><span class="t-lg">people’s</span></span>
      <span class="line"><span class="t-lg green">lives</span><span class="t-xs"> through </span><span class="t-lg cyan">innovation</span></span>
      <span class="line"><span class="t-md">in research, </span><span class="t-md crimson">education</span></span>
      <span class="line"><span class="t-md">and </span><span class="t-lg yellow">patient care</span></span>
    </h1>

    <div class="video-box" role="img" aria-label="Video preview showing a white tree illustration on a dark background">
      <div class="play-button">
        <svg width="18" height="18" viewBox="0 0 18 18"><polygon points="2,0 18,9 2,18" fill="#1d7fc0"/></svg>
      </div>
    </div>

    <div class="brand-band"></div>
    <div class="brand">
      <span class="brand-mark"></span>
      <span class="brand-name">Wardline Systems</span>
    </div>
    <p class="brand-tagline">improving patient care</p>

    <nav class="menu">
      <div class="tile cable">Cable<br>TV</div>
      <div class="tile movies">Movies</div>
      <div class="tile welcome">Welcome</div>
      <div class="tile campus small">Campus<br>Map</div>
      <div class="tile chart small">Ardent<br>Chart</div>
      <div class="tile light small phones">Important<br>Phone<br>Numbers</div>
      <div class="tile light dining">Dining<br>Options</div>
      <div class="tile light small education">Patient<br>Education<br>Materials</div>
      <div class="tile light services">Request<br>Services</div>
    </nav>
  </main>
</body>
</html>
```